Destination Wedding Photographer

I am a Wedding photographer based in San Juan, Puerto Rico. The banner will be shown in the United States to brides that plan to have their wedding in Puerto Rico.

I want to highlight the following words/phrases
Puerto Rico
Destination Wedding
Photographer
(in that order)

feel free to get creative adding your own inspired text.

My web site: www.renzomalvek.com

Target Market(s)

Brides in the united states looking for a photographer for their wedding in Puerto Rico

Industry/Entity Type

Wedding

Requirements
Must have
• + Your ad must be a .gif, .png or .jpg smaller than 40kb in filesize
+ include the following sizes: 300x250, 728x90, 160x600, 468x60, or 120x600
+ Your ad must include the advertiser's brand
+ Your ad must have a border
Should not have
• + Your ad cannot imitate computer effects like scrolling or mousing over
+ No animations longer than 30 seconds
+ No strobe or flashing effects allowed
+ Your ad and campaign must not feature or promote alcohol, anabolic steroids, drugs, financial products, gambling, adult content, or weight loss products

```html
<!DOCTYPE html>
<html lang="en">
<head>
<meta charset="utf-8">
<title>Renzo Malvek Photography – Destination Wedding Photographer</title>
<link rel="stylesheet" href="https://fonts.googleapis.com/css2?family=Arimo:wght@400;700&family=Great+Vibes&display=swap">
<style>
  :root {
    --sky-top: #3b3f48;
    --sky-mid: #5d636d;
    --sea-dark: #23282f;
    --sea-mid: #3a414b;
    --couple-warm: #8a7a70;
    --text-light: #ffffff;
    --button-bg: #ffffff;
    --button-text: #000000;
    --border: #1a1a1a;
  }
  * { box-sizing: border-box; margin: 0; padding: 0; }
  html, body { width: 1200px; height: 148px; overflow: hidden; background: #fff; }
  .banner {
    position: relative;
    width: 1200px;
    height: 148px;
    border: 2px solid var(--border);
    overflow: hidden;
    font-family: "Arimo", Arial, sans-serif;
    color: var(--text-light);
  }
  .seascape {
    position: absolute; inset: 0;
    background:
      linear-gradient(180deg, var(--sky-top) 0%, var(--sky-mid) 42%, var(--sea-mid) 55%, var(--sea-dark) 100%);
  }
  .couple {
    position: absolute;
    left: 560px; top: 0;
    width: 170px; height: 148px;
    background: radial-gradient(ellipse at 50% 55%, var(--couple-warm) 0%, rgba(90,85,84,0.6) 55%, rgba(60,63,70,0) 100%);
  }
  .headline { position: absolute; left: 12px; top: 4px; line-height: 1; }
  .headline .script {
    font-family: "Great Vibes", cursive;
    font-size: 68px;
    font-weight: 400;
  }
  .headline .small { font-size: 24px; }
  .headline .line-two { position: absolute; left: 74px; top: 82px; white-space: nowrap; }
  .headline .place { font-size: 34px; }
  .headline .line-one { white-space: nowrap; }
  .brand {
    position: absolute; left: 760px; top: 28px;
    font-size: 30px; font-weight: 400; letter-spacing: 1px;
    white-space: nowrap;
  }
  .brand-mark {
    display: inline-block; width: 10px; height: 10px;
    border-radius: 50%; background: var(--text-light);
    margin-left: 8px; vertical-align: middle;
  }
  .tagline {
    position: absolute; left: 682px; top: 110px;
    font-size: 20px; white-space: nowrap;
  }
  .contact {
    position: absolute; left: 1028px; top: 61px;
    width: 152px; height: 30px;
    background: var(--button-bg); color: var(--button-text);
    font-size: 18px; font-weight: 700;
    display: flex; align-items: center; justify-content: center; gap: 6px;
  }
  .contact svg { width: 11px; height: 13px; }
</style>
</head>
<body>
  <div class="banner">
    <div class="seascape" role="img" aria-label="Dusk photo of the ocean with waves under a grey sky"></div>
    <div class="couple" role="img" aria-label="Photo of a bride and groom embracing on the beach"></div>

    <div class="headline">
      <div class="line-one"><span class="script">Wedding Dreams</span> <span class="small">become</span></div>
      <div class="line-two"><span class="small">reality in</span> <span class="place">Puerto Rico</span></div>
    </div>

    <div class="brand">Renzo Malvek Photography<span class="brand-mark"></span></div>
    <div class="tagline">Destination Wedding Photographer</div>

    <div class="contact">Contact Now
      <svg viewBox="0 0 11 13" aria-hidden="true"><polygon points="0,0 11,6.5 0,13" fill="currentColor"/></svg>
    </div>
  </div>
</body>
</html>
```